Mining and Labour hire business needs website

need a web page for a business located in country NSW,Australia. we provide labour hire with a background in electrical contracting. i've attached images that i would like used. and a text file with the text to be used

Target Market(s)

mining and resource sector

Industry/Entity Type

Business

Requirements
Must have
• my logo
• Pages: main, about us, labour hire services, electrical services, equipment, employment, contact us
Nice to have
• other photos/images of heavy industry/mining
• background photos in black and white would be good i think.
• photo sliders

```html
<!DOCTYPE html>
<html lang="en">
<head>
<meta charset="utf-8">
<title>Karra Industry Services</title>
<link rel="stylesheet" href="https://fonts.googleapis.com/css2?family=Oswald:wght@400;500&family=Roboto:wght@400;500&display=swap">
<style>
:root{
  --gold:#c9a35c;
  --gold-dark:#b88f47;
  --ink:#1c1c1c;
  --text:#555;
  --muted:#777;
  --grey-band:#eeeeee;
  --white:#fff;
  --footer-bar:#111;
}
*{box-sizing:border-box;margin:0;padding:0}
html,body{width:670px;height:1200px;overflow:hidden;background:var(--white)}
body{position:relative;font-family:"Roboto",Arial,sans-serif;color:var(--text)}
.abs{position:absolute}

/* header */
.site-header{left:0;top:0;width:670px;height:56px;background:var(--white);box-shadow:0 1px 3px rgba(0,0,0,.12);z-index:2}
.brand{left:50px;top:16px;display:flex;align-items:center;gap:7px}
.brand-square{width:22px;height:22px;background:var(--ink)}
.brand-name{font-weight:500;font-size:12px;letter-spacing:.8px;color:var(--ink);text-transform:uppercase}
.main-nav{right:84px;top:27px;display:flex;gap:19px;font-size:7.6px;color:var(--ink);text-transform:uppercase}
.main-nav .active{color:var(--gold)}
.search-btn{left:600px;top:22px;width:21px;height:20px;border:1px solid #ddd;display:flex;align-items:center;justify-content:center}

/* hero */
.hero{left:0;top:56px;width:670px;height:357px;background:linear-gradient(180deg,#8fb4db 0%,#c4d6e6 42%,#8c8f8e 58%,#3a3c3d 80%,#222 100%)}
.hero-caption{left:49px;top:230px;width:229px;height:102px;background:rgba(0,0,0,.72);padding:14px 0 0 15px}
.hero-kicker{font-family:"Oswald",sans-serif;font-size:21px;color:var(--white);line-height:1}
.hero-title{font-family:"Oswald",sans-serif;font-size:38px;color:var(--gold);line-height:1.15;margin-top:6px}
.hero-arrows{left:51px;top:345px;display:flex;gap:3px}
.hero-arrow{width:20px;height:20px;border-radius:50%;background:rgba(0,0,0,.55);display:flex;align-items:center;justify-content:center}

/* features */
.features{left:0;top:413px;width:670px;height:197px;background:var(--gold)}
.feature{width:180px;text-align:center;color:var(--white)}
.feature-icon{width:52px;height:52px;border:1.5px solid var(--white);border-radius:50%;margin:0 auto;display:flex;align-items:center;justify-content:center}
.feature h3{font-weight:400;font-size:10px;margin:11px 0 6px;letter-spacing:.4px}
.feature p{font-size:6.3px;line-height:1.7}
.btn-outline{display:inline-block;margin-top:8px;border:1px solid var(--white);border-radius:3px;font-size:6px;padding:4px 8px}

/* welcome */
.video-frame{left:49px;top:641px;width:242px;height:150px;border:1px solid #ddd;padding:3px;background:var(--white)}
.video-still{width:100%;height:100%;background:linear-gradient(160deg,#f3b16a 0%,#c46128 45%,#6f2f12 80%,#2a1c14 100%);position:relative}
.play{position:absolute;left:96px;top:50px;width:44px;height:44px;border-radius:50%;background:rgba(0,0,0,.55);display:flex;align-items:center;justify-content:center}
.welcome{left:310px;top:645px;width:315px}
.section-title{font-size:13px;color:var(--gold);font-weight:400;text-transform:uppercase}
.welcome h3{font-weight:400;font-size:9.5px;color:var(--ink);margin:6px 0 10px}
.welcome p,.what-we-do p{font-size:6.5px;line-height:1.8;color:var(--muted)}
.welcome p+p{margin-top:10px}
.btn-gold{display:inline-block;background:var(--gold);color:var(--white);font-size:6.8px;font-weight:500;padding:6px 13px;border-radius:2px;text-transform:uppercase;box-shadow:0 1px 0 var(--gold-dark)}

/* what we do */
.band-grey{left:3px;top:829px;width:667px;height:201px;background:var(--grey-band)}
.what-we-do{left:50px;top:862px;width:372px}
.what-we-do p{margin:12px 0 14px}
.wwd-brand{left:460px;top:905px;width:150px;display:flex;align-items:center;gap:8px}
.wwd-brand .brand-square{width:26px;height:26px}
.wwd-brand .brand-name{font-size:14px;line-height:1.2}

/* footer */
.site-footer{left:0;top:1030px;width:670px;height:132px;background:var(--gold);color:var(--white)}
.footer-col{top:24px}
.footer-col h4{font-weight:400;font-size:9.8px;text-transform:uppercase;margin-bottom:10px}
.footer-col p{font-size:6.5px;line-height:1.65}
.email-field{width:120px;height:18px;margin-top:9px;background:#f1f1f1;border:1px solid #ccc;color:#555;font-size:6.5px;padding:4px 6px}
.btn-dark{display:inline-block;margin-top:7px;background:var(--ink);color:var(--white);font-size:6.5px;padding:5px 8px;border-radius:2px;text-transform:uppercase}
.tweet{display:flex;gap:5px;margin-bottom:11px}
.tweet-dot{width:7px;height:7px;border-radius:50%;background:var(--white);flex:none;margin-top:2px}
.tweet em{font-style:italic}
.social{display:flex;align-items:center;gap:10px;font-size:6.6px;margin-bottom:6px}
.social-ring{width:18px;height:18px;border:1px solid rgba(255,255,255,.75);border-radius:50%}
.copyright-bar{left:0;top:1162px;width:670px;height:38px;background:var(--footer-bar);color:var(--white);font-size:6.5px;text-align:center;line-height:38px}
</style>
</head>
<body>

<header class="site-header abs">
  <div class="brand abs"><span class="brand-square"></span><span class="brand-name">Karra Industry Services</span></div>
  <nav class="main-nav abs">
    <span class="active">Home</span><span>Services</span><span>Portfolio</span><span>Solutions</span><span>Jobs</span><span>Blog</span><span>Contacts</span>
  </nav>
  <div class="search-btn abs">
    <svg width="8" height="8" viewBox="0 0 10 10"><circle cx="4" cy="4" r="3" fill="none" stroke="#1c1c1c" stroke-width="1.6"/><line x1="6.2" y1="6.2" x2="9" y2="9" stroke="#1c1c1c" stroke-width="1.8"/></svg>
  </div>
</header>

<section class="hero abs" role="img" aria-label="Mining processing plant with conveyor gantry and stockpiles under a blue sky">
</section>
<div class="hero-caption abs">
  <div class="hero-kicker">We start work with</div>
  <div class="hero-title">GREAT VISION</div>
</div>
<div class="hero-arrows abs">
  <span class="hero-arrow"><svg width="7" height="7" viewBox="0 0 8 8"><polyline points="5.5,1 2.5,4 5.5,7" fill="none" stroke="#fff" stroke-width="1.4"/></svg></span>
  <span class="hero-arrow"><svg width="7" height="7" viewBox="0 0 8 8"><polyline points="2.5,1 5.5,4 2.5,7" fill="none" stroke="#fff" stroke-width="1.4"/></svg></span>
</div>

<section class="features abs">
  <div class="feature abs" style="left:44px;top:31px">
    <div class="feature-icon"><svg width="20" height="18" viewBox="0 0 20 18"><rect x="1" y="1" width="18" height="12" rx="1" fill="none" stroke="#fff" stroke-width="2"/><rect x="8" y="13" width="4" height="3" fill="#fff"/><rect x="5" y="16" width="10" height="2" fill="#fff"/></svg></div>
    <h3>PLANING</h3>
    <p>Lorem Ipsum has been the industry's standard<br>dummy text ever since the 1500s, when an unknown<br>printer took a galley of type and scrambled book</p>
    <span class="btn-outline">Read More ▸</span>
  </div>
  <div class="feature abs" style="left:244px;top:33px">
    <div class="feature-icon"><svg width="20" height="18" viewBox="0 0 20 18"><polygon points="1,8 19,1 13,17 9,11" fill="#fff"/><polyline points="19,1 9,11" stroke="#c9a35c" stroke-width="1.2"/></svg></div>
    <h3>DESIGN</h3>
    <p>Lorem Ipsum has been the industry's standard<br>dummy text ever since the 1500s, when an unknown<br>printer took a galley of type and scrambled book</p>
    <span class="btn-outline">Read More ▸</span>
  </div>
  <div class="feature abs" style="left:446px;top:31px">
    <div class="feature-icon"><svg width="22" height="16" viewBox="0 0 22 16"><rect x="4" y="1" width="14" height="10" rx="1" fill="none" stroke="#fff" stroke-width="1.8"/><rect x="1" y="12" width="20" height="2.5" rx="1" fill="#fff"/></svg></div>
    <h3>CODING</h3>
    <p>Lorem Ipsum has been the industry's standard<br>dummy text ever since the 1500s, when an unknown<br>printer took a galley of type and scrambled book</p>
    <span class="btn-outline">Read More ▸</span>
  </div>
</section>

<div class="video-frame abs">
  <div class="video-still" role="img" aria-label="Rusted industrial headframe wall glowing orange at sunset, video preview">
    <span class="play"><svg width="16" height="18" viewBox="0 0 16 18"><polygon points="2,1 15,9 2,17" fill="#fff"/></svg></span>
  </div>
</div>
<section class="welcome abs">
  <h2 class="section-title">Welcome to Karraindustryservices</h2>
  <h3>Neque porro quisquam est qui dolorem ipsum quia dolor sit amet</h3>
  <p>Lorem Ipsum has been the industry's standard dummy text ever since the 1500s, when an unknown printer took a galley of type and scrambled it to make a type specimen book. It has survived not only five centuries, but also the leap into electronic typesetting, remaining essentially unchanged.</p>
  <p>It was popularised in the 1960s with the release of Letterfold sheets containing Lorem Ipsum passages, and more recently with desktop publishing software like Pressline Composer including versions</p>
  <span class="btn-gold" style="margin-top:13px">Read More</span>
</section>

<div class="band-grey abs"></div>
<section class="what-we-do abs">
  <h2 class="section-title">What We Do</h2>
  <p>Lorem Ipsum has been the industry's standard dummy text ever since the 1500s, when an unknown printer took a galley of type and scrambled it to make a type specimen book. It has survived not only five centuries, but also the leap into electronic typesetting, remaining essentially unchanged. It was popularised in the 1960s with the release of Letterfold sheets containing Lorem Ipsum passages, and more recently with desktop publishing software like Pressline Composer including versions of Lorem Ipsum</p>
  <span class="btn-gold">Read More</span>
</section>
<div class="wwd-brand abs"><span class="brand-square"></span><span class="brand-name">Karra Industry Services</span></div>

<footer class="site-footer abs">
  <div class="footer-col abs" style="left:52px">
    <h4>Newsletters Sign Up</h4>
    <p>Sign up for our daily email by entering<br>your information below</p>
    <div class="email-field">Email address</div>
    <span class="btn-dark">Subscribe</span>
  </div>
  <div class="footer-col abs" style="left:219px">
    <h4>Latest Tweet</h4>
    <div class="tweet"><span class="tweet-dot"></span><p>Featured Workspace : Ironmill<br>ironm.il/4Rk2Ta <em>10 hours ago</em></p></div>
    <div class="tweet"><span class="tweet-dot"></span><p>Featured Workspace : Ironmill<br>ironm.il/4Rk2Ta <em>10 hours ago</em></p></div>
  </div>
  <div class="footer-col abs" style="left:385px">
    <h4>Get In Touch</h4>
    <p>Address : 14 Quarry Road,<br>Westbrook, NSW</p>
    <p style="margin-top:10px">Phone : 02 5550 1834</p>
    <p style="margin-top:10px">Email : info@karra-works.com</p>
  </div>
  <div class="footer-col abs" style="left:540px">
    <h4>Follow Us On</h4>
    <div class="social"><span class="social-ring"></span>Friendwall</div>
    <div class="social"><span class="social-ring"></span>Chirpline</div>
    <div class="social"><span class="social-ring"></span>Photostream</div>
  </div>
</footer>
<div class="copyright-bar abs">Copyright © 2015. All Rights Reserved</div>

</body>
</html>
```